Webdesign für einen  Bauträger und Projektentwickler
Webdesign für einen Bauträger und Projektentwickler
Zielgruppe
Wir sind ein Bauträger und Projektentwickler aus Ulm. Kapitalanleger sind hauptsächlich unsere Zielgruppe.
Aufgabenstellung
Die bereits bestehende Webseite soll überarbeitet werden bzw. das Design & Layout soll modernisiert werden. Das Design soll edel und klassisch sein. Die Webseite soll Menschen anziehen, die wertige Immobilien oder Bauprojekte suchen. Das Design sollte bevorzugt mit dem Tool Adobe Photoshop erstellt werden. Das Unternehmenslogo wurde kürzlich überarbeitet, wurde jedoch noch nicht gelauncht. Dies soll mit der überarbeiteten Webseite geschehen.

```html
<!DOCTYPE html>
<html lang="de">
<head>
<meta charset="utf-8">
<title>Kontakt – Hofkar Gruppe</title>
<link href="https://fonts.googleapis.com/css2?family=Karla:wght@400;500;700&display=swap" rel="stylesheet">
<style>
:root{
  --ink:#111;
  --muted:#8a8a8a;
  --accent:#f2d21b;
  --panel:#f2f2f2;
  --footer:#efefef;
  --line:#dadada;
  --white:#fff;
}
*{box-sizing:border-box;margin:0;padding:0}
html,body{width:901px;height:1200px;overflow:hidden;background:var(--white)}
body{position:relative;font-family:'Karla',sans-serif;color:var(--ink);font-size:8.3px;line-height:1.5}
.abs{position:absolute}
.brand{font-weight:700;font-size:18px;line-height:1;color:var(--ink);display:flex;align-items:center;gap:7px}
.brand-mark{width:12px;height:12px;background:var(--accent)}
.nav a{position:absolute;top:23px;font-size:9px;font-weight:700;color:var(--ink);text-decoration:none}
.nav a.active::after{content:"";position:absolute;left:0;right:0;top:13px;height:2px;background:var(--accent)}
.hero{left:0;top:65px;width:901px;height:185px;background:linear-gradient(90deg,#bdbdbd 0%,#8c5f5a 30%,#a23a44 50%,#6e4a44 75%,#3d2a28 100%)}
.crumb{left:176px;top:266px;font-size:8.5px;font-weight:700}
.crumb span{color:var(--muted)}
h1{position:absolute;left:176px;top:300px;font-size:19px;font-weight:700;letter-spacing:.5px;line-height:1}
.bar{position:absolute;height:2px;background:var(--accent)}
h3{font-size:8.5px;font-weight:700;margin-bottom:4px}
.info p{line-height:13px}
.ico{display:inline-block;width:7px;height:7px;vertical-align:-1px;margin-right:3px}
.panel{left:176px;top:463px;width:548px;height:495px;background:var(--panel)}
h2{position:absolute;left:223px;top:503px;font-size:13px;font-weight:700;letter-spacing:.3px;line-height:1}
label{position:absolute;font-size:8.3px}
.field{position:absolute;background:var(--white);border:1px solid var(--line)}
.select{color:var(--muted);padding:8px 6px;font-size:8.3px}
.select svg{position:absolute;right:9px;top:11px}
.consent{left:223px;top:829px;width:456px;font-size:8.3px;line-height:13px}
.consent i{display:inline-block;width:8px;height:8px;border:1px solid #555;background:var(--white);margin-right:4px;vertical-align:-1px}
.consent u{text-underline-offset:1px}
.btn{left:618px;top:897px;width:60px;height:27px;background:var(--accent);font-size:8.3px;font-weight:500;text-align:center;line-height:27px}
.footer{left:0;top:1010px;width:901px;height:146px;background:var(--footer)}
.footer p,.links p{line-height:13px}
.legal{left:176px;top:1170px;font-size:8.3px}
.rating{left:399px;top:1170px;font-size:7px}
.rating b{font-size:8px;letter-spacing:.5px;margin-right:3px}
.social{top:1168px;width:19px;height:19px;border-radius:50%;background:var(--accent)}
</style>
</head>
<body>
<header>
  <div class="abs brand" style="left:177px;top:24px"><span class="brand-mark"></span>Hofkar</div>
  <nav class="nav">
    <a style="left:399px">Projekte</a>
    <a style="left:456px">Hofkar Gruppe</a>
    <a style="left:535px">Immobilien-Blog</a>
    <a style="left:628px">Aktuelles</a>
    <a class="active" style="left:690px">Kontakt</a>
  </nav>
</header>

<div class="abs hero" role="img" aria-label="Foto: Terrasse eines Cafés mit Rattanstühlen und roten Lamellenwänden"></div>

<div class="abs crumb"><span>Startseite</span> &nbsp;⟶&nbsp; Kontakt</div>

<h1>Kontakt</h1>
<div class="bar" style="left:177px;top:330px;width:36px"></div>

<section class="abs info" style="left:177px;top:354px">
  <h3>Kontaktdaten</h3>
  <p>Hofkar Gruppe<br>Brunnenweg 12<br>89075 Ulm</p>
  <p style="margin-top:4px"><svg class="ico" viewBox="0 0 10 10"><path d="M2 0.5l2 2-1 1.2a6 6 0 0 0 3.3 3.3l1.2-1 2 2-1.2 1.5C4 9 1 6 0.5 1.7z" fill="#111"/></svg>0171 987 6543<br>
  <svg class="ico" viewBox="0 0 10 8"><rect width="10" height="8" fill="#111"/><path d="M0.5 0.8l4.5 3.5 4.5-3.5" stroke="#fff" fill="none" stroke-width="1"/></svg>info@hofkarsp.de</p>
</section>

<section class="abs info" style="left:362px;top:354px">
  <h3>Öffnungszeiten</h3>
  <p>Montag - Donnerstag:<br>8.00 - 12.00 Uhr und 13.00 - 18.00 Uhr</p>
  <p style="margin-top:9px">Freitag:<br>8.00 - 12.00 Uhr</p>
</section>

<div class="abs panel"></div>
<h2>Kontakt aufnehmen</h2>
<div class="bar" style="left:224px;top:524px;width:35px"></div>

<label style="left:224px;top:546px">Anrede*</label>
<div class="field select" style="left:223px;top:559px;width:223px;height:28px">Bitte auswählen
  <svg width="7" height="5" viewBox="0 0 7 5"><path d="M0.7 0.7l2.8 2.8 2.8-2.8" stroke="#111" stroke-width="1.4" fill="none"/></svg></div>
<label style="left:455px;top:546px">Vorname, Nachname*</label>
<div class="field" style="left:455px;top:559px;width:223px;height:28px"></div>

<label style="left:224px;top:596px">Telefonnummer*</label>
<div class="field" style="left:223px;top:610px;width:223px;height:27px"></div>
<label style="left:455px;top:596px">E-Mail-Adresse*</label>
<div class="field" style="left:455px;top:610px;width:223px;height:27px"></div>

<label style="left:224px;top:646px">Ihre Nachricht*</label>
<div class="field" style="left:223px;top:660px;width:455px;height:159px"></div>

<p class="abs consent"><i></i>Ja, ich habe die <u>Datenschutzerklärung</u> zur Kenntnis genommen und bin damit einverstanden, dass die von mir angegebenen Daten elektronisch erhoben und gespeichert werden. Meine Daten werden dabei nur streng zweckgebunden zur Bearbeitung und Beantwortung meiner Anfrage benutzt. Mit dem Absenden des Kontaktformulars erkläre ich mich mit der Verarbeitung einverstanden. *</p>

<div class="abs btn">Absenden</div>

<footer>
  <div class="abs footer"></div>
  <div class="abs brand" style="left:176px;top:1036px"><span class="brand-mark"></span>Hofkar</div>
  <p class="abs" style="left:177px;top:1069px;width:190px;line-height:13px">Seit mehr als 30 Jahren schaffen wir nicht nur Gebäude. Als Bauträger haben wir, die Hofkar Gruppe, es uns zur Aufgabe gemacht, Ihre Wohnträume zu verwirklichen und einzigartige Investitionsobjekte zu schaffen.</p>
  <section class="abs info" style="left:456px;top:1036px">
    <h3 style="margin-bottom:6px">Kontakt</h3>
    <p>Hofkar Gruppe<br>Brunnenweg 12<br>89075 Ulm</p>
    <p style="margin-top:4px"><svg class="ico" viewBox="0 0 10 10"><path d="M2 0.5l2 2-1 1.2a6 6 0 0 0 3.3 3.3l1.2-1 2 2-1.2 1.5C4 9 1 6 0.5 1.7z" fill="#111"/></svg>0171 987 6543<br>
    <svg class="ico" viewBox="0 0 10 8"><rect width="10" height="8" fill="#111"/><path d="M0.5 0.8l4.5 3.5 4.5-3.5" stroke="#fff" fill="none" stroke-width="1"/></svg>info@hofkarsp.de</p>
  </section>
  <section class="abs links" style="left:595px;top:1036px">
    <h3 style="margin-bottom:6px">Menü</h3>
    <p>Startseite<br>Projekte<br>Hofkar Gruppe<br>Immobilien-Blog<br>Aktuelles</p>
  </section>
  <div class="abs legal">Impressum | Datenschutz | AGB</div>
  <div class="abs rating"><b>★★★★★</b>4,8 von 5 Sternen</div>
  <div class="abs social" style="left:658px" role="img" aria-label="Soziales Netzwerk"></div>
  <div class="abs social" style="left:682px" role="img" aria-label="Soziales Netzwerk"></div>
  <div class="abs social" style="left:706px" role="img" aria-label="Videoplattform"></div>
</footer>
</body>
</html>
```